Harlowe plumbing business cards

Want a functional designed for my business cards using my logo

Company Name- Harlowe Plumbing, Heating & Water Systems
Name- Marcus Harlowe
Title- Vice President
Cell- 555-318-7426
Email- Harloweplumbing@mailbrook.net
Business address-
PO Box 37
Fenwick Mill, MD 21999

Industry/Entity Type

Plumbing

```html
<!DOCTYPE html>
<html lang="en">
<head>
<meta charset="utf-8">
<title>Harlowe Plumbing – Business Card</title>
<link rel="stylesheet" href="https://fonts.googleapis.com/css2?family=Roboto:wght@700&family=Open+Sans:wght@400&display=swap">
<style>
  :root {
    --page-bg: #e8e9eb;
    --card-dark: #3a3a3c;
    --card-blue: #0a70c2;
    --pipe-light: #93afe0;
    --text-white: #ffffff;
    --text-soft: #f1f5fb;
  }
  * { margin: 0; padding: 0; box-sizing: border-box; }
  html, body {
    width: 1200px;
    height: 900px;
    overflow: hidden;
    background: var(--page-bg);
  }
  .canvas {
    position: relative;
    width: 1200px;
    height: 900px;
  }
  .business-card {
    position: absolute;
    left: 120px;
    top: 154px;
    width: 960px;
    height: 592px;
    overflow: hidden;
    box-shadow: 0 10px 30px rgba(0,0,0,0.18);
  }
  .card-artwork {
    position: absolute;
    inset: 0;
    width: 100%;
    height: 100%;
    display: block;
  }
  .contact-block {
    position: absolute;
    left: 113px;
    top: 0;
    color: var(--text-white);
    font-family: "Open Sans", Arial, sans-serif;
  }
  .person-name {
    position: absolute;
    top: 239px;
    left: 0;
    white-space: nowrap;
    font-family: "Roboto", Arial, sans-serif;
    font-weight: 700;
    font-size: 32px;
    letter-spacing: 0.3px;
  }
  .person-title {
    position: absolute;
    top: 276px;
    left: 0;
    white-space: nowrap;
    font-size: 23px;
    color: var(--text-soft);
  }
  .address-line,
  .contact-line {
    position: absolute;
    left: 0;
    white-space: nowrap;
    font-size: 24px;
    color: var(--text-soft);
  }
  .address-line.po-box { top: 334px; }
  .address-line.city { top: 368px; }
  .contact-line {
    left: -6px;
    display: flex;
    align-items: center;
    gap: 6px;
  }
  .contact-line.office { top: 436px; }
  .contact-line.mobile { top: 470px; }
  .contact-line.email { top: 506px; }
  .contact-icon {
    width: 20px;
    height: 20px;
    flex: none;
    fill: var(--text-white);
  }
  .company-name {
    position: absolute;
    left: 560px;
    width: 370px;
    top: 208px;
    text-align: center;
    color: var(--text-white);
    font-family: "Open Sans", Arial, sans-serif;
    font-weight: 400;
  }
  .company-name .brand {
    display: block;
    font-size: 44px;
    line-height: 1.1;
    white-space: nowrap;
  }
  .company-name .tagline {
    display: block;
    font-size: 26px;
    line-height: 1.3;
    white-space: nowrap;
  }
</style>
</head>
<body>
<main class="canvas">
  <section class="business-card" aria-label="Harlowe Plumbing business card">
    <svg class="card-artwork" viewBox="0 0 652 402" preserveAspectRatio="none" aria-hidden="true">
      <rect class="card-dark-field" x="0" y="0" width="652" height="402" fill="var(--card-dark)"/>
      <polygon class="card-blue-field" points="0,169 24,169 24,100 344,100 344,247 652,247 652,402 0,402" fill="var(--card-blue)"/>
      <polygon class="pipe-band" points="24,169 24,100 344,100 344,247 652,247 652,297 320,297 320,120 44,120 44,169" fill="var(--pipe-light)"/>
      <path class="water-drop" d="M18 178 C 24 208, 46 230, 46 260 A 28 28 0 0 1 -10 260 C -10 230, 12 208, 18 178 Z" fill="var(--pipe-light)"/>
    </svg>

    <div class="company-name">
      <span class="brand">Harlowe Plumbing</span>
      <span class="tagline">Heating &amp; Water Systems</span>
    </div>

    <div class="contact-block">
      <h1 class="person-name">MARCUS HARLOWE</h1>
      <p class="person-title">Vice President</p>
      <p class="address-line po-box">PO Box 37</p>
      <p class="address-line city">Fenwick Mill, MD 21999</p>
      <p class="contact-line office">
        <svg class="contact-icon" viewBox="0 0 20 20" aria-hidden="true"><path d="M2 7 C2 4 5 3 10 3 C15 3 18 4 18 7 L18 8 L14 8 L13 6 L7 6 L6 8 L2 8 Z M5 10 L15 10 L17 17 L3 17 Z"/></svg>
        555.204.6613
      </p>
      <p class="contact-line mobile">
        <svg class="contact-icon" viewBox="0 0 20 20" aria-hidden="true"><path d="M6 1 H14 A2 2 0 0 1 16 3 V17 A2 2 0 0 1 14 19 H6 A2 2 0 0 1 4 17 V3 A2 2 0 0 1 6 1 Z M6 3.5 V14.5 H14 V3.5 Z M10 15.6 A1.1 1.1 0 1 0 10 17.8 A1.1 1.1 0 1 0 10 15.6 Z"/></svg>
        555-318-7426
      </p>
      <p class="contact-line email">
        <svg class="contact-icon" viewBox="0 0 20 20" aria-hidden="true"><path d="M2 5 H18 V15 H2 Z M3 6 L10 11 L17 6 L17 6.8 L10 12 L3 6.8 Z" fill-rule="evenodd"/></svg>
        Harloweplumbing@mailbrook.net
      </p>
    </div>
  </section>
</main>
</body>
</html>
```